Design eines Hausetiketts für traditionelles Weingut
Zielgruppe
Wir das Familienweingut Brosowski in Gimbsheim/Rheinhessen sind ein traditionelles Weingut das seine Reben selbst kultiviert und die Weine auch selbst ausbaut. Wir haben jeden Schritt in der Weinherstellung selbst in der Hand und vermarkten den Wein dann an unsere Privatkunden. Unsere Kundenstruktur sieht folgendermaßen aus: Wir haben 100% Privatkunden die unseren Wein konsumieren. Da jetzt die nächste Generation in den Weinbaubetrieb einsteigt und auch Ideen hat möchten wir ein Hausetikett einführen. Im Moment haben wir noch sehr viele unterschiedliche Etiketten und kein Hausetikett. Da die Verlagsetiketten immer seltener zu unseren Vorstellungen passen, möchten wir hier auf diesem Wege ein Hausetikett anfertigen lassen. Generell möchten wir unseren Außenauftritt komplett modernisieren. Sie können sich über die Vielfalt in unserem Betrieb unter www.weingut-brosowski-beispiel.de einen Überblick verschaffen. Langfristig gesehen wollen wir aber unsere Weinkarte verkleinern.
Aufgabenstellung
Wir haben uns vor ca. 1,5 Jahren hier auf dieser Website bereits ein Logo designen lassen. Es wäre schön wenn man das Logo bei den Entwürfen für die Etiketten berücksichtigen würde. Das wäre aber KEIN MUSS. Auch wäre es gut wenn man das ,,Wein' bei unserem Namen weglassen könnte.
Das Etikett sollte aus Vorder-und Rückenetikett bestehen und edel wirken. Vorne sollte die Rebsorte und die Geschmacksangabe stehen. Der Rest sollte auf das Rückenetikett.
Das Vorderetikett sollte ein richtiger Eyecatcher sein und im Supermarkt z.B. aus vielen anderen herausstechen. Das wäre ganz wichtig.
Man kann bei den Farben unterscheiden in 3 Konzepte.
Literwein als einsteiger Wein
Dann die Gutsweine und zum Schluss die Lagenweine. Alles Farblich oder im design etwas abgesetzt.

```html
<!DOCTYPE html>
<html lang="de">
<head>
<meta charset="utf-8">
<title>Brosowski Familienweingut – Chardonnay Spätlese</title>
<link href="https://fonts.googleapis.com/css2?family=Cinzel:wght@400;500&family=Heebo:wght@400&display=swap" rel="stylesheet">
<style>
  :root {
    --paper: #faeede;
    --gold: #a47a45;
    --ink: #1e1a17;
    --grey: #8c9098;
    --brown: #6a3f16;
    --red: #e0161f;
  }
  html, body {
    margin: 0;
    padding: 0;
    width: 1200px;
    height: 792px;
    overflow: hidden;
    background: var(--paper);
  }
  .label {
    position: relative;
    width: 1200px;
    height: 792px;
    background: var(--paper);
  }
  .label > * {
    position: absolute;
    margin: 0;
    white-space: nowrap;
  }
  .centered {
    left: 0;
    width: 1200px;
    text-align: center;
  }
  .estate-name {
    top: 188px;
    font-family: "Cinzel", serif;
    font-weight: 400;
    font-size: 68px;
    line-height: 1;
    letter-spacing: 0.01em;
    color: var(--gold);
  }
  .estate-type {
    top: 262px;
    font-family: "Cinzel", serif;
    font-size: 24px;
    line-height: 1;
    letter-spacing: 0.24em;
    color: var(--ink);
  }
  .divider {
    top: 312px;
    left: 300px;
    width: 600px;
    height: 1.5px;
    background: linear-gradient(90deg, var(--ink) 0%, var(--ink) 55%, var(--gold) 100%);
  }
  .origin {
    top: 342px;
    font-family: "Cinzel", serif;
    font-size: 22px;
    line-height: 1;
    letter-spacing: 0.06em;
    color: var(--grey);
  }
  .variety {
    top: 434px;
    font-family: "Heebo", sans-serif;
    font-weight: 400;
    font-size: 42px;
    line-height: 1;
    color: var(--brown);
  }
  .vineyard {
    top: 504px;
    font-family: "Cinzel", serif;
    font-size: 16px;
    line-height: 1;
    letter-spacing: 0.08em;
    color: var(--grey);
  }
  .taste {
    top: 578px;
    font-family: "Cinzel", serif;
    font-size: 21px;
    line-height: 1;
    color: var(--red);
  }
  .vintage {
    top: 650px;
    font-family: "Cinzel", serif;
    font-size: 78px;
    line-height: 1;
    color: var(--red);
  }
  .volume, .alcohol {
    top: 702px;
    font-family: "Heebo", sans-serif;
    font-size: 25px;
    line-height: 1;
    color: var(--brown);
  }
  .volume { left: 232px; }
  .alcohol { right: 199px; }
</style>
</head>
<body>
  <main class="label">
    <h1 class="estate-name centered">BROSOWSKI</h1>
    <p class="estate-type centered">FAMILIENWEINGUT</p>
    <div class="divider"></div>
    <p class="origin centered">GIMBSHEIM — RHEINHESSEN</p>
    <h2 class="variety centered">Chardonnay Spätlese</h2>
    <p class="vineyard centered">GIMBSHEIMER SONNENWEG</p>
    <p class="taste centered">TROCKEN</p>
    <p class="vintage centered">2018</p>
    <p class="volume">0,75 l</p>
    <p class="alcohol">12,5 %</p>
  </main>
</body>
</html>
```